Business Card for staff member of football club SC Brenval

I would like to get a business card template for all staff member of our soccer club.

The card should use as much as possible the 2 colors of the club : Red which is the main color and blue which is the alternative color. It can be balanced between the two like our logo.

I prefer simple and lean design.

Contact Information for Business Card

Bussiness card should have all main stuff as describe here below in must have.

Font styles to use
Sans Serif

Requirements
Must have
• Name : Laurent DESPRATIN
Fonction : Président
Mobile : +41 xx xxx xx xx
Email : first.lastname@scbrenval.ch
Adresse of the club : SC Brenval, 1873 Brenval
Website of the club : www.scbrenval.ch
Nice to have
• Version with and without picture of the staff member

A version for men, a version for women staff member.

```html
<!DOCTYPE html>
<html lang="fr">
<head>
<meta charset="utf-8">
<title>SC Brenval – Carte de visite</title>
<link rel="stylesheet" href="https://fonts.googleapis.com/css2?family=Oswald:wght@700&family=Montserrat:ital,wght@0,400;0,700;1,400&display=swap">
<style>
  :root {
    --club-red: #e31b37;
    --club-blue: #0a86cf;
    --ink: #111111;
    --muted: #6b6b6b;
    --text: #333333;
    --card-white: #ffffff;
    --card-black: #161616;
    --stage: #2a2a2a;
    --photo-light: #eef0f2;
    --photo-dark: #2b2c33;
  }
  html, body {
    margin: 0;
    width: 1200px;
    height: 900px;
    overflow: hidden;
    background: var(--stage);
  }
  .stage {
    width: 1200px;
    height: 900px;
    display: flex;
    flex-direction: column;
    align-items: center;
    justify-content: center;
    gap: 44px;
  }
  .card {
    position: relative;
    width: 700px;
    height: 400px;
    box-sizing: border-box;
    overflow: hidden;
    box-shadow: 0 10px 30px rgba(0,0,0,.45);
  }
  /* Front */
  .card--front {
    background: var(--card-white);
  }
  .front__club {
    position: absolute;
    left: 44px;
    top: 30px;
    margin: 0;
    font-family: "Oswald", sans-serif;
    font-weight: 700;
    font-size: 72px;
    line-height: 1;
    letter-spacing: -1px;
    text-transform: uppercase;
    color: var(--ink);
    white-space: nowrap;
  }
  .front__name {
    position: absolute;
    left: 46px;
    top: 132px;
    margin: 0;
    font-family: "Montserrat", sans-serif;
    font-weight: 700;
    font-size: 22px;
    color: var(--club-blue);
    white-space: nowrap;
  }
  .front__role {
    position: absolute;
    left: 46px;
    top: 162px;
    margin: 0;
    font-family: "Montserrat", sans-serif;
    font-style: italic;
    font-size: 15px;
    color: var(--muted);
  }
  .contact {
    position: absolute;
    left: 46px;
    top: 214px;
    margin: 0;
    padding: 0;
    list-style: none;
    font-family: "Montserrat", sans-serif;
    font-size: 15px;
    color: var(--text);
  }
  .contact__item {
    display: flex;
    align-items: center;
    gap: 10px;
    height: 27px;
    white-space: nowrap;
  }
  .contact__icon {
    width: 14px;
    height: 14px;
    flex: none;
    fill: var(--club-red);
  }
  .front__photo {
    position: absolute;
    right: 0;
    bottom: 0;
    width: 300px;
    height: 270px;
    background: linear-gradient(180deg, var(--photo-light) 0%, #c9b8aa 45%, var(--photo-dark) 100%);
  }
  /* Back */
  .card--back {
    background: var(--card-black);
    display: flex;
    align-items: center;
    justify-content: center;
    gap: 22px;
  }
  .back__dot {
    width: 56px;
    height: 56px;
    border-radius: 50%;
    background: var(--club-red);
  }
  .back__club {
    margin: 0;
    font-family: "Oswald", sans-serif;
    font-weight: 700;
    font-size: 76px;
    line-height: 1;
    letter-spacing: -1px;
    text-transform: uppercase;
    color: #ffffff;
    white-space: nowrap;
  }
</style>
</head>
<body>
<main class="stage">
  <section class="card card--front" aria-label="Recto de la carte">
    <h1 class="front__club">SC Brenval</h1>
    <p class="front__name">Laurent DESPRATIN</p>
    <p class="front__role">Président</p>
    <ul class="contact">
      <li class="contact__item">
        <svg class="contact__icon" viewBox="0 0 14 14" aria-hidden="true"><path d="M4 0h6a1.5 1.5 0 0 1 1.5 1.5v11A1.5 1.5 0 0 1 10 14H4a1.5 1.5 0 0 1-1.5-1.5v-11A1.5 1.5 0 0 1 4 0zm0 2v9h6V2zm3 9.6a.9.9 0 1 0 0 1.8.9.9 0 0 0 0-1.8z"/></svg>
        <span>+41 27 481 05 36</span>
      </li>
      <li class="contact__item">
        <svg class="contact__icon" viewBox="0 0 14 14" aria-hidden="true"><path d="M0 3h14v8H0zm1.2 1 5.8 4 5.8-4z" fill-rule="evenodd"/></svg>
        <span>first.lastname@scbrenval.ch</span>
      </li>
      <li class="contact__item">
        <svg class="contact__icon" viewBox="0 0 14 14" aria-hidden="true"><circle cx="7" cy="7" r="6.5"/><path d="M.5 7h13M7 .5c-3 3.5-3 9.5 0 13M7 .5c3 3.5 3 9.5 0 13" stroke="#fff" stroke-width="1" fill="none"/></svg>
        <span>www.scbrenval.ch</span>
      </li>
      <li class="contact__item">
        <svg class="contact__icon" viewBox="0 0 14 14" aria-hidden="true"><path d="M7 0a4.8 4.8 0 0 1 4.8 4.8C11.8 8.5 7 14 7 14S2.2 8.5 2.2 4.8A4.8 4.8 0 0 1 7 0zm0 3a1.8 1.8 0 1 0 0 3.6A1.8 1.8 0 0 0 7 3z"/></svg>
        <span>SC Brenval, 1873 Brenval</span>
      </li>
    </ul>
    <div class="front__photo" role="img" aria-label="Portrait photo of the staff member in a suit and tie"></div>
  </section>

  <section class="card card--back" aria-label="Verso de la carte">
    <span class="back__dot" aria-hidden="true"></span>
    <p class="back__club">SC Brenval</p>
  </section>
</main>
</body>
</html>
```